Bubble map/flip book

I need someone to create a bubble map with explanations using the attached. This will be used to create a color coded flip book/manual. I need you to clean this up.

Dorothywinslade@postlark.com

```html
<!DOCTYPE html>
<html lang="en">
<head>
<meta charset="utf-8">
<title>Claim Denial Flip Book</title>
<link rel="stylesheet" href="https://fonts.googleapis.com/css2?family=Open+Sans:wght@400;600;700;800&display=swap">
<style>
:root{
  --stage:#8c8c8c;
  --ink:#2b2b2b;
  --black:#222226;
  --yellow:#ffd200;
  --amber:#f7a800;
  --pink:#e6176a;
  --crimson:#cf1040;
  --green:#4a7a2a;
  --forest:#1f3d10;
  --brown:#8a5a14;
  --umber:#5a3208;
  --purple:#5a2a9a;
  --navy:#1a1060;
  --blue:#0d4f9a;
  --orange:#f07d1a;
  --red:#e0401a;
}
*{margin:0;padding:0;box-sizing:border-box}
html,body{width:944px;height:1200px;overflow:hidden;background:var(--stage);font-family:"Open Sans",Arial,sans-serif;color:var(--ink)}
.sheet{position:relative;width:944px;height:1200px}
.page{position:absolute;width:211px;height:274px;overflow:hidden;
  background:linear-gradient(180deg,#ffffff 0%,#fbfbfc 55%,#eceef2 100%)}
.page::after{content:"";position:absolute;right:0;bottom:0;width:30px;height:30px;
  background:var(--corner);clip-path:polygon(100% 0,100% 100%,0 100%)}
.wires{position:absolute;left:0;top:0;width:211px;height:274px}
.bar{position:absolute;left:14px;width:184px;height:29px;display:flex;align-items:center;justify-content:center;
  text-align:center;color:#fff;font-weight:700;font-size:7px;line-height:1.25;box-shadow:0 1.5px 0 rgba(0,0,0,.25)}
.bar.dark{color:#2a2a2a}
.box{position:absolute;display:flex;align-items:center;justify-content:center;text-align:center;
  font-weight:700;font-size:3.3px;line-height:1.22;padding:1.5px;color:#fff;overflow:hidden}
.box > span{display:block;width:100%}
.box.dark{color:#2a2a2a}
.box em{font-style:italic}
.title{position:absolute;left:0;width:211px;text-align:center;font-weight:700;font-size:8.4px;line-height:1.2}
.rule{position:absolute;height:2.6px}
.doc{position:absolute;font-size:2.7px;line-height:1.4;color:#333}
.doc p{margin-bottom:1.2px}
.doc ul{list-style:none;margin-bottom:1.2px}
.doc .lead{font-weight:700}
.side{position:absolute;font-size:3.2px;line-height:1.3;font-weight:700;color:var(--blue)}
.sub{position:absolute;font-size:4.4px;font-weight:700;color:var(--blue)}
</style>
</head>
<body>
<svg width="0" height="0" style="position:absolute">
  <defs>
    <marker id="ar-amber" viewBox="0 0 6 6" refX="6" refY="3" markerWidth="3" markerHeight="3" markerUnits="userSpaceOnUse" orient="auto"><path d="M0 0L6 3L0 6z" fill="#f7a800"/></marker>
    <marker id="ar-crimson" viewBox="0 0 6 6" refX="6" refY="3" markerWidth="3" markerHeight="3" markerUnits="userSpaceOnUse" orient="auto"><path d="M0 0L6 3L0 6z" fill="#cf1040"/></marker>
    <marker id="ar-green" viewBox="0 0 6 6" refX="6" refY="3" markerWidth="3" markerHeight="3" markerUnits="userSpaceOnUse" orient="auto"><path d="M0 0L6 3L0 6z" fill="#4a7a2a"/></marker>
    <marker id="ar-brown" viewBox="0 0 6 6" refX="6" refY="3" markerWidth="3" markerHeight="3" markerUnits="userSpaceOnUse" orient="auto"><path d="M0 0L6 3L0 6z" fill="#8a5a14"/></marker>
    <marker id="ar-purple" viewBox="0 0 6 6" refX="6" refY="3" markerWidth="3" markerHeight="3" markerUnits="userSpaceOnUse" orient="auto"><path d="M0 0L6 3L0 6z" fill="#1a1060"/></marker>
    <marker id="ar-blue" viewBox="0 0 6 6" refX="6" refY="3" markerWidth="3" markerHeight="3" markerUnits="userSpaceOnUse" orient="auto"><path d="M0 0L6 3L0 6z" fill="#0d4f9a"/></marker>
    <marker id="ar-orange" viewBox="0 0 6 6" refX="6" refY="3" markerWidth="3" markerHeight="3" markerUnits="userSpaceOnUse" orient="auto"><path d="M0 0L6 3L0 6z" fill="#e0401a"/></marker>
  </defs>
</svg>

<main class="sheet">

<!-- Overview -->
<section class="page" style="left:40px;top:46px;--corner:var(--yellow)">
  <svg class="wires" viewBox="0 0 211 274">
    <g stroke-width=".6">
      <line x1="28" y1="62" x2="28" y2="130" stroke="#ffd200"/>
      <line x1="54" y1="62" x2="54" y2="182" stroke="#e6176a"/>
      <line x1="80" y1="62" x2="80" y2="130" stroke="#4a7a2a"/>
      <line x1="106" y1="62" x2="106" y2="182" stroke="#8a5a14"/>
      <line x1="131" y1="62" x2="131" y2="130" stroke="#5a2a9a"/>
      <line x1="158" y1="62" x2="158" y2="182" stroke="#0d4f9a"/>
      <line x1="183" y1="62" x2="183" y2="130" stroke="#f07d1a"/>
    </g>
    <g>
      <circle cx="28" cy="63" r="1.3" fill="#ffd200"/><circle cx="54" cy="63" r="1.3" fill="#e6176a"/>
      <circle cx="80" cy="63" r="1.3" fill="#4a7a2a"/><circle cx="106" cy="63" r="1.3" fill="#8a5a14"/>
      <circle cx="131" cy="63" r="1.3" fill="#5a2a9a"/><circle cx="158" cy="63" r="1.3" fill="#0d4f9a"/>
      <circle cx="183" cy="63" r="1.3" fill="#f07d1a"/>
    </g>
  </svg>
  <div class="bar" style="top:32px;background:var(--black);font-size:8.4px;font-weight:600;letter-spacing:.2px">CLAIM HAS BEEN DENIED</div>
  <div class="box" style="left:9px;top:130px;width:38px;height:40px;background:var(--yellow);color:#9a7a00;font-size:4px;font-weight:400"><span>Authorization/ Referral Needed</span></div>
  <div class="box" style="left:60px;top:130px;width:39px;height:40px;background:var(--green);font-size:4px;font-weight:400"><span>Duplicate</span></div>
  <div class="box" style="left:112px;top:130px;width:39px;height:40px;background:var(--purple);font-size:4px;font-weight:400"><span>Global Inclusive</span></div>
  <div class="box" style="left:163px;top:130px;width:39px;height:40px;background:var(--orange);color:#fde2c8;font-size:4px;font-weight:400"><span>Past Timely Filing</span></div>
  <div class="box" style="left:34px;top:182px;width:40px;height:39px;background:var(--pink);font-size:4px;font-weight:400"><span>Coding/ Billing Issues</span></div>
  <div class="box" style="left:86px;top:182px;width:40px;height:39px;background:var(--brown);font-size:4px;font-weight:400"><span>Non-Covered Charge</span></div>
  <div class="box" style="left:138px;top:182px;width:40px;height:39px;background:var(--blue);font-size:4px;font-weight:400"><span>Additional Information Requested</span></div>
</section>

<!-- Authorization flow -->
<section class="page" style="left:258px;top:46px;--corner:var(--yellow)">
  <svg class="wires" viewBox="0 0 211 274" fill="none" stroke="#f7a800" stroke-width=".6">
    <path d="M103 98V108M48 108H166"/>
    <line x1="48" y1="108" x2="48" y2="120" marker-end="url(#ar-amber)"/>
    <line x1="166" y1="108" x2="166" y2="120" marker-end="url(#ar-amber)"/>
    <line x1="27" y1="165" x2="27" y2="186" marker-end="url(#ar-amber)"/>
    <line x1="77" y1="165" x2="77" y2="186" marker-end="url(#ar-amber)"/>
    <line x1="137" y1="165" x2="137" y2="186" marker-end="url(#ar-amber)"/>
    <line x1="187" y1="165" x2="187" y2="186" marker-end="url(#ar-amber)"/>
  </svg>
  <div class="bar dark" style="top:32px;background:var(--yellow)">Claim denied for no authorization/referral.</div>
  <div class="box dark" style="left:56px;top:74px;width:94px;height:24px;background:var(--yellow);font-weight:400;font-size:3.6px"><span>Contact carrier.<br><em>Was claim processed in network or out of network?</em></span></div>
  <div class="box dark" style="left:13px;top:120px;width:71px;height:45px;background:var(--yellow)"><span>Claim processed correctly as in network provider. Medical records printed and sent for medical necessity.</span></div>
  <div class="box dark" style="left:131px;top:120px;width:71px;height:45px;background:var(--amber)"><span>Claim processed out of network. Contact with carrier shows claim processed as out of network in error.<br><em>Will representative send the claim back for review?</em></span></div>
  <div class="box dark" style="left:12px;top:186px;width:30px;height:47px;background:var(--yellow)"><span>Appeal denied as services were not arranged. Balance is patient responsibility</span></div>
  <div class="box dark" style="left:62px;top:186px;width:30px;height:47px;background:var(--yellow)"><span>Appeal for claim paid.</span></div>
  <div class="box dark" style="left:122px;top:186px;width:30px;height:47px;background:var(--amber)"><span>Claim has been sent back for review. Follow up in 14 days.</span></div>
  <div class="box dark" style="left:172px;top:186px;width:30px;height:47px;background:var(--amber)"><span>Representative will not send the claim back for review. Appeal sent to carrier. Follow up in 30 days.</span></div>
</section>

<!-- Authorization notes -->
<section class="page" style="left:478px;top:46px;--corner:var(--yellow)">
  <div class="title" style="top:42px;color:var(--amber);font-weight:600">Authorization/referral needed.</div>
  <div class="rule" style="left:33px;top:56px;width:146px;background:var(--yellow)"></div>
  <div class="doc" style="left:38px;top:68px;width:140px">
    <p>1. If you are a network provider verify that the claim processed correctly in network. If it was processed out of network have the claim sent back to process or send appeal stating the claim processed out of network.</p>
    <p>2. If you are not a network provider you may send an appeal with medical records attached stating to reprocess and pay claim in network.</p>
    <p class="lead">NOTES ON ACCOUNT SHOULD INCLUDE:</p>
    <ul><li>- Claim number</li><li>- Denial date</li><li>- Processed in or out of network</li></ul>
  </div>
</section>

<!-- Coding flow -->
<section class="page" style="left:696px;top:46px;--corner:var(--pink)">
  <svg class="wires" viewBox="0 0 211 274" fill="none" stroke="#cf1040" stroke-width=".6">
    <path d="M105 98V108M50 108H163"/>
    <line x1="50" y1="108" x2="50" y2="120" marker-end="url(#ar-crimson)"/>
    <line x1="163" y1="108" x2="163" y2="120" marker-end="url(#ar-crimson)"/>
    <line x1="140" y1="167" x2="140" y2="186" marker-end="url(#ar-crimson)"/>
    <line x1="188" y1="167" x2="188" y2="186" marker-end="url(#ar-crimson)"/>
  </svg>
  <div class="bar" style="top:32px;background:var(--pink)">Coding Denial<br>CPT/DX/Modifier</div>
  <div class="box" style="left:57px;top:74px;width:97px;height:24px;background:var(--pink);font-weight:400;font-size:3.8px"><span>Contact made with carrier.</span></div>
  <div class="box" style="left:16px;top:120px;width:69px;height:47px;background:var(--pink)"><span>Claim denied in error and has been sent back to process.</span></div>
  <div class="box" style="left:129px;top:120px;width:69px;height:47px;background:var(--crimson)"><span>Claim denied correctly for coding error</span></div>
  <div class="box" style="left:126px;top:186px;width:28px;height:47px;background:var(--crimson)"><span>Forwarded to physician for review</span></div>
  <div class="box" style="left:174px;top:186px;width:28px;height:47px;background:var(--crimson)"><span>Corrected and rebilled as a corrected claim</span></div>
</section>

<!-- Coding notes -->
<section class="page" style="left:40px;top:326px;--corner:var(--pink)">
  <div class="title" style="top:44px;color:var(--pink);font-weight:600">Coding Denial</div>
  <div class="rule" style="left:33px;top:58px;width:146px;background:var(--pink)"></div>
  <div class="doc" style="left:56px;top:68px;width:112px">
    <p class="lead">Example:</p>
    <p>*Claim denied as procedure code used 99203 is for a new patient and this is an established patient.</p>
    <p class="lead">ACCOUNT NOTE WILL INCLUDE:</p>
    <ul>
      <li>*How information was obtained</li><li>*Name of representative</li><li>*Claim number</li><li>*Denial date</li>
      <li>*What was denied: CPT, HCPCS, modifier, diagnosis?</li><li>*What code denied?</li><li>*Why was it denied?</li>
      <li>A. Not covered?</li><li>B. Bundled to another code on the claim? Which code is it bundled with?</li>
      <li>C. Not a covered benefit per patient policy? What is the service?</li><li>D. Invalid modifier? What modifier was billed?</li>
      <li>E. Diagnosis does not match CPT? Verify codes billed.</li><li>*Appeal address</li><li>*Timely filing</li>
    </ul>
    <p style="margin-top:4px">*Verify that the claim was billed with the CPT code stated.</p>
  </div>
</section>

<!-- Duplicate flow -->
<section class="page" style="left:258px;top:326px;--corner:var(--green)">
  <svg class="wires" viewBox="0 0 211 274" fill="none" stroke="#4a7a2a" stroke-width=".6">
    <path d="M101 98V108M47 108H164"/>
    <line x1="47" y1="108" x2="47" y2="120" marker-end="url(#ar-green)"/>
    <line x1="164" y1="108" x2="164" y2="120" marker-end="url(#ar-green)"/>
    <line x1="27" y1="162" x2="27" y2="186" marker-end="url(#ar-green)"/>
    <line x1="77" y1="162" x2="77" y2="186" marker-end="url(#ar-green)"/>
  </svg>
  <div class="bar" style="top:32px;background:var(--green)">Claim denied as a duplicate</div>
  <div class="box" style="left:58px;top:76px;width:87px;height:22px;background:var(--green);font-weight:400;font-size:3.6px"><span>Verify that your office has not sent two claims for this date of service</span></div>
  <div class="box" style="left:12px;top:120px;width:70px;height:42px;background:var(--green)"><span>Only 1 claim billed. Contact with carrier shows other claim billed under a different NPI or Tax ID.<br><em>Will representative send claim back to process?</em></span></div>
  <div class="box" style="left:129px;top:120px;width:70px;height:42px;background:var(--forest)"><span>Two claims billed. If additional charges were added combine charges and rebill as corrected claim. If two identical claims sent in error void claim.</span></div>
  <div class="box" style="left:12px;top:186px;width:30px;height:47px;background:var(--green)"><span>Rep. sent claim back to process for payment</span></div>
  <div class="box" style="left:62px;top:186px;width:30px;height:47px;background:var(--green)"><span>Rep. will not send claim back to process. Send appeal with medical records</span></div>
</section>

<!-- Non-covered flow -->
<section class="page" style="left:478px;top:326px;--corner:var(--brown)">
  <svg class="wires" viewBox="0 0 211 274" fill="none" stroke="#8a5a14" stroke-width=".6">
    <path d="M106 98V108M52 108H164"/>
    <line x1="52" y1="108" x2="52" y2="120" marker-end="url(#ar-brown)"/>
    <line x1="164" y1="108" x2="164" y2="120" marker-end="url(#ar-brown)"/>
    <line x1="29" y1="172" x2="29" y2="197" marker-end="url(#ar-brown)"/>
    <line x1="79" y1="172" x2="79" y2="197" marker-end="url(#ar-brown)"/>
  </svg>
  <div class="bar" style="top:32px;background:var(--brown)">Claim denied as Non-covered</div>
  <div class="box" style="left:58px;top:74px;width:96px;height:24px;background:var(--brown);font-weight:400;font-size:3.8px"><span>Contact Carrier.</span></div>
  <div class="box" style="left:17px;top:120px;width:70px;height:52px;background:var(--brown)"><span>Claim denied correctly. What is non-covered:<br><em>The diagnosis or CPT Code?</em><br><em>Is the diagnosis a policy exclusion (Exp – Obesity related Dx)</em><br><em>Send back to the physician to see if diagnosis can be changed</em></span></div>
  <div class="box" style="left:129px;top:120px;width:70px;height:52px;background:var(--umber)"><span>Claim denied in error and claim has been sent back to process</span></div>
  <div class="box" style="left:14px;top:197px;width:30px;height:36px;background:var(--brown)"><span>Dx updated and claim rebilled as corrected claim</span></div>
  <div class="box" style="left:64px;top:197px;width:30px;height:36px;background:var(--brown)"><span>Physician unable to change Dx - Appeal with medical records</span></div>
</section>

<!-- Global inclusive flow -->
<section class="page" style="left:696px;top:326px;--corner:var(--purple)">
  <svg class="wires" viewBox="0 0 211 274" fill="none" stroke="#1a1060" stroke-width=".6">
    <path d="M106 62V100M50 100H162"/>
    <line x1="50" y1="100" x2="50" y2="117" marker-end="url(#ar-purple)"/>
    <line x1="162" y1="100" x2="162" y2="117" marker-end="url(#ar-purple)"/>
  </svg>
  <div class="bar" style="top:32px;background:var(--purple)">Claim denied as Global Inclusive</div>
  <div class="box" style="left:17px;top:117px;width:67px;height:58px;background:var(--purple)"><span>Claim denied and has been sent back to process</span></div>
  <div class="box" style="left:129px;top:117px;width:67px;height:58px;background:var(--navy)"><span>Claim is global inclusive to claim resolved accounts</span></div>
</section>

<!-- Global surgical package -->
<section class="page" style="left:40px;top:607px;--corner:var(--purple)">
  <div class="title" style="top:38px;color:var(--purple);font-size:7.6px">GLOBAL SURGICAL PACKAGE</div>
  <div class="rule" style="left:33px;top:51px;width:146px;background:var(--purple)"></div>
  <div class="doc" style="left:50px;top:61px;width:124px">
    <ul>
      <li>• The global surgical package is a single payment for all care associated with a surgical procedure. Within 90 days.</li>
      <li>• Other names for the Global Surgical Package include: Postoperative Period, Global Period, Global Services, Surgical Period, Global package and Global Surgery.</li>
      <li>• Care of a patient during the global surgical period is not restricted to any specific location. A patient may be treated by the surgeon or another provider of the same medical group and specialty in any location including inpatient, outpatient, ambulatory surgical center, nursing home, emergency room or urgent care.</li>
    </ul>
  </div>
  <div class="title" style="top:140px;color:var(--purple);font-size:7.6px">NO CHARGE SERVICES</div>
  <div class="rule" style="left:33px;top:153px;width:146px;background:var(--purple)"></div>
  <div class="doc" style="left:50px;top:165px;width:124px">
    <p>There are several services that are not charged services as they are associated with another service.</p>
    <ul style="padding-left:6px">
      <li>• Suture removal placed at this office</li><li>• Routine ER follow up</li><li>• Sputum follow up</li><li>• Corneal abrasion follow up</li>
    </ul>
  </div>
</section>

<!-- Additional information flow -->
<section class="page" style="left:258px;top:607px;--corner:var(--blue)">
  <svg class="wires" viewBox="0 0 211 274" fill="none" stroke="#0d4f9a" stroke-width=".6">
    <path d="M105 62V108M78 108H148"/>
    <line x1="78" y1="108" x2="78" y2="118" marker-end="url(#ar-blue)"/>
    <line x1="148" y1="108" x2="148" y2="118" marker-end="url(#ar-blue)"/>
    <path d="M78 160V214H93" marker-end="url(#ar-blue)"/>
    <path d="M140 160V183H125" marker-end="url(#ar-blue)"/>
    <path d="M156 160V214H125" marker-end="url(#ar-blue)"/>
  </svg>
  <div class="bar" style="top:32px;background:var(--blue)">Additional Information Requested</div>
  <div class="side" style="left:22px;top:126px">* Primary<br>EOB<br><br>* Medical<br>Records</div>
  <div class="box" style="left:62px;top:118px;width:32px;height:42px;background:var(--blue)"><span>Additional information requested from provider.<br><br><span style="font-weight:400">See Attachment</span></span></div>
  <div class="box" style="left:133px;top:118px;width:32px;height:42px;background:var(--navy)"><span>Additional information requested from patient.<br><br><span style="font-weight:400">See Attachment</span></span></div>
  <div class="side" style="left:171px;top:122px">* COB<br>Update<br><br>* Third party<br>liability form</div>
  <div class="box" style="left:94px;top:166px;width:31px;height:34px;background:var(--blue)"><span>Applied to patient responsibility</span></div>
  <div class="box" style="left:94px;top:204px;width:31px;height:22px;background:var(--blue)"><span>Claim paid</span></div>
</section>

<!-- Patient information questions -->
<section class="page" style="left:478px;top:607px;--corner:var(--blue)">
  <div class="title" style="top:32px;color:var(--blue);font-size:6.4px;line-height:1.3">Claim has been denied requesting<br>additional information from the patient:</div>
  <div class="rule" style="left:34px;top:53px;width:144px;background:var(--blue)"></div>
  <div class="doc" style="left:38px;top:66px;width:140px">
    <p class="lead" style="color:var(--blue)">Carrier Questions for note:</p>
    <ul>
      <li>*Who did you speak to?</li><li>*What is the phone number?</li><li>*What is the claim number?</li><li>*When did the claim deny?</li>
      <li>*What has been requested from the patient? When was the patient last contacted?</li><li>*How can the patient respond to your request? Fax? Phone? Mail?</li>
    </ul>
    <p>*Claim denied for Third Party Liability Form: verify the service performed was not due to an injury by going to the history tab and checking for an accident date. If services were not for an injury, send the claim back to process.</p>
    <p>*Claim denied for Coordination of Benefits update: ask what other carrier they are showing on file.</p>
    <p>*Claim denied for missing or incomplete policy information. What is missing?</p>
    <p>*Make sure it is displayed on the account. This will create a note every time someone goes into the account.</p>
    <p>*Add your note to the account. Account note should end with printed letter to patient.</p>
    <p>*Set next action code to pending information from patient. Set follow up for 2 weeks.</p>
    <p>*Specialist will send the patient letter and note the account.</p>
    <p>*Follow up on the account in 2 weeks. If patient has not responded move balance to patient responsibility.</p>
  </div>
</section>

<!-- Pending from patient (TPL) -->
<section class="page" style="left:696px;top:607px;--corner:var(--blue)">
  <div class="title" style="top:24px;color:var(--blue);font-size:6.4px">Pending Information from the Patient</div>
  <div class="rule" style="left:24px;top:34px;width:164px;background:var(--blue)"></div>
  <div class="doc" style="left:26px;top:40px;width:160px;font-size:2.5px">
    <p>1) Claim has been denied or pended by the carrier requesting additional information from the patient.</p>
    <p class="lead" style="padding-left:5px">What is included in account note:</p>
    <ul style="padding-left:5px">
      <li>*How information was obtained</li><li>*Phone number</li><li>*Claim number</li><li>*Denial date</li>
      <li>*What has been requested from the patient</li><li>*When was the patient last contacted</li><li>*How can the patient respond to request</li><li>*Timely filing limit</li>
    </ul>
    <p>2) Third Party Liability Form / Accident Details (TPL)</p>
    <ul style="padding-left:5px">
      <li>a. Verify via the history tab that the service performed was not due to an injury.</li>
      <li>b. Check the diagnosis code and confirm why the patient was seen.</li>
      <li>c. If claim was accurately denied for TPL, print the form letter from the patient chart.</li>
      <li>d. Print the populated letter to the printer.</li>
      <li>e. Note the account that the TPL letter has been printed.</li>
      <li>f. Staff will initiate the account once the letter is sent.</li>
      <li>g. Add a memo to the patient chart indicating the letter was sent.</li>
      <li>h. Set the next action code to pending information from patient. Set follow up for 2 weeks.</li>
      <li>i. If two weeks have passed with no response, resend the letter directly to the patient.</li>
      <li>j. If TPL details have been updated by the carrier, note the account accordingly.</li>
      <li>k. Remove the previous memo from the patient account.</li>
      <li>l. Follow up on the account in 2 weeks.</li>
      <li>m. If TPL details have not been updated, move the balance to patient responsibility.</li>
    </ul>
  </div>
</section>

<!-- Pending from patient (COB) -->
<section class="page" style="left:40px;top:888px;--corner:var(--blue)">
  <div class="title" style="top:22px;color:var(--blue);font-size:6.4px">Pending Information from the Patient</div>
  <div class="rule" style="left:24px;top:32px;width:164px;background:var(--blue)"></div>
  <div class="doc" style="left:26px;top:40px;width:160px;font-size:2.45px">
    <p>1) Coordination of Benefits (COB) details</p>
    <ul style="padding-left:5px">
      <li>a. Request for the carrier to validate those details have not been updated already.</li>
      <li>i. If they have not, please proceed to submit the COB letter to the patient.</li>
      <li>1. If claim was accurately denied for COB, in the patient chart select the COB letter.</li>
      <li>2. Print the populated form letter to the printer.</li>
      <li>3. Notate the account that the COB letter has been printed.</li>
      <li>4. Staff will notate the account once the letter is sent.</li>
      <li>5. Add a memo to the patient chart indicating the COB letter was sent.</li>
      <li>6. Set next action code to pending information from patient. Set follow up for 2 weeks.</li>
      <li>7. If two weeks have passed, resend the letter directly to the patient.</li>
      <li>8. If COB details have been updated by the carrier, note the account.</li>
      <li>9. Remove the previous memo from the patient account.</li>
      <li>10. If COB details have not been updated, move balance to patient.</li>
    </ul>
    <p>2) Coverage termination effective for the date of service</p>
    <ul style="padding-left:5px">
      <li>a. If the carrier states there was no coverage for the date of service.</li>
      <li>i. Please identify the date that coverage terminated.</li>
      <li>ii. If the patient never showed as having coverage, please confirm you have the right patient.</li>
      <li>iii. Populate and print the insurance not in effect letter to the patient.</li>
      <li>iv. If there is no response from the patient in two weeks, move balance to patient.</li>
      <li>v. If the patient responds to the letter, update the insurance and rebill.</li>
    </ul>
  </div>
</section>

<!-- Pending from provider -->
<section class="page" style="left:258px;top:888px;--corner:var(--blue)">
  <div class="title" style="top:30px;color:var(--blue);font-size:6.4px">Pending information from provider</div>
  <div class="rule" style="left:34px;top:41px;width:144px;background:var(--blue)"></div>
  <div class="sub" style="left:38px;top:54px">Primary EOB required</div>
  <div class="doc" style="left:38px;top:66px;width:136px">
    <p class="lead">Account note will include:</p>
    <ul>
      <li>*How information was obtained</li><li>*Name of representative</li><li>*Phone number</li><li>*Claim number</li><li>*Denial date</li><li>*Name of primary carrier on file</li>
    </ul>
    <p style="margin-top:3px">1. Claim has previously been billed to the primary carrier. Print EOB and rebill with claim.</p>
    <p>2. Claim was not sent to primary carrier. Send claim to that carrier.</p>
    <p>3. Claim was not billed to primary carrier as the patient did not inform clinic of other insurance coverage. Representative supplies primary carrier on file. Call will be made to the carrier to verify ID number, group number, effective dates and claim address. Insurance information will be added to patient information and claim will be sent.</p>
    <p>4. Claim was not billed to the primary carrier; representative did not give other health insurance information. Patient will be sent Coordination of Benefits letter.</p>
  </div>
</section>

<!-- Timely filing flow -->
<section class="page" style="left:478px;top:888px;--corner:var(--orange)">
  <svg class="wires" viewBox="0 0 211 274" fill="none" stroke="#e0401a" stroke-width=".6">
    <path d="M35 90H168"/>
    <line x1="35" y1="90" x2="35" y2="104" marker-end="url(#ar-orange)"/>
    <line x1="168" y1="90" x2="168" y2="104" marker-end="url(#ar-orange)"/>
    <line x1="104" y1="64" x2="104" y2="158" marker-end="url(#ar-orange)"/>
    <line x1="104" y1="210" x2="104" y2="237" marker-end="url(#ar-orange)"/>
  </svg>
  <div class="bar" style="top:34px;background:var(--orange)">Claim/appeal denied for past timely filing.</div>
  <div class="box" style="left:16px;top:104px;width:37px;height:44px;background:var(--orange)"><span>Claim is not past timely filing and rep. sends claim back to process.</span></div>
  <div class="box" style="left:150px;top:104px;width:37px;height:44px;background:var(--red)"><span>Account is past filing deadline.</span></div>
  <div class="box" style="left:86px;top:158px;width:36px;height:52px;background:var(--red)"><span>Rep. will not send claim back to process, but you find proof that claim was not past filing deadline.</span></div>
  <div class="box" style="left:86px;top:237px;width:36px;height:23px;background:var(--red)"><span>Timely filing appeal sent.</span></div>
</section>

<!-- Timely filing notes -->
<section class="page" style="left:696px;top:888px;--corner:var(--orange)">
  <div class="title" style="top:44px;color:var(--orange);font-weight:600">Past Timely Filing</div>
  <div class="rule" style="left:33px;top:58px;width:146px;background:var(--orange)"></div>
  <div class="doc" style="left:58px;top:70px;width:118px">
    <p>* Carrier filing limits:</p>
    <ul style="padding-left:6px">
      <li>Silverpath Senior Plan: Claim 90 days appeals 180 days</li><li>Crestline Health: Claim 120 days appeals 180 days</li><li>Harborview Mutual: Claim 90 days</li>
      <li>Northgate Benefits: Claim 90 days appeals 180 days</li><li>Maplewood Care: Claim 180 days</li><li>State Assist Plan: Claim 90 days appeals 10 months</li>
      <li>Federal Elder Plan: 365 days</li><li>Unionfield Health: Claim 90 days</li><li>Service Member Plan: 365 days</li>
    </ul>
    <p class="lead" style="margin-top:2px">Account notes will include</p>
    <ul style="padding-left:4px">
      <li>* Claim number</li><li>* Denial date</li><li>* Date the claim/appeal was received</li><li>* Filing deadline</li>
      <li>* Date original (first) claim or appeal was received?</li><li>* Appeal address</li><li>* Appeal timely filing</li>
    </ul>
    <p style="margin-top:3px">* Claim is not past timely filing have the representative send the claim back to process.</p>
    <p>* If rep. will not send claim back to process. Send appeal.</p>
  </div>
</section>

</main>
</body>
</html>
```